Sea Larq (www.sealarq.com) web site development

Sea Larq is a new Fishing, Spearfishing Charter operator offering private charters in North Belize, Turneffe, Lighthouse Reef and the Blue Hole. The logo of the company has been designed by Artflocker, some months ago. We have also developed a small brochure which can be the base for the website development (at least colors, fonts, etc.).
Pictures and Video should be an important asset of this website. We need to be able to update contents (video, photos), update prices and destinations, etc.

Target Market(s)

High hand, fishing and spearfishing enthusiasts.

Industry/Entity Type

Yacht charter

Coding

Coded - Design and coding required

Number of Pages Required

4 page

Colors
EB3D1F
EC4F4E
F09395
F8D3D4
FCEDEE

Requirements
Must have
• Optimized for phone and tablet navigation, must be easy to update with photos and video, connected to our Instagram and Facebook page,

```html
<!DOCTYPE html>
<html lang="en">
<head>
<meta charset="utf-8">
<title>Sea Larq — Fishing &amp; Spearfishing Charters</title>
<link rel="stylesheet" href="https://fonts.googleapis.com/css2?family=Barlow:wght@400;500;600;700&family=Barlow+Semi+Condensed:ital,wght@0,700;1,800&display=swap">
<style>
:root{
  --teal:#1d4656;
  --teal-dark:#153542;
  --red:#e8262f;
  --red-soft:#ec4f4e;
  --light:#f1f2f3;
  --white:#ffffff;
  --ink:#233038;
  --muted:#6c7a82;
  --sea:#3f7f95;
  --sea-light:#7fb3c4;
}
*{margin:0;padding:0;box-sizing:border-box}
html,body{width:1200px;height:3480px;overflow:hidden;background:var(--white)}
body{font-family:"Barlow",Arial,sans-serif;color:var(--ink);font-size:15px;line-height:1.6}
.heading{font-family:"Barlow Semi Condensed","Arial Narrow",sans-serif;font-style:italic;font-weight:800;letter-spacing:.3px}
.eyebrow{color:var(--red);font-size:12px;font-weight:700;text-transform:uppercase;letter-spacing:2px}
.btn{display:inline-block;background:var(--teal);color:var(--white);font-weight:600;font-size:13px;padding:10px 24px;border-radius:2px}
.btn-red{background:var(--red)}
.photo{border-radius:2px}

.top-bar{height:30px;background:var(--teal-dark);color:#cfdde3;font-size:12px;display:flex;align-items:center;gap:28px;padding:0 80px}
.site-nav{height:70px;display:flex;align-items:center;justify-content:space-between;padding:0 80px;background:var(--white);border-bottom:1px solid #e3e6e8}
.brand{display:flex;align-items:center;gap:10px}
.brand-dot{width:26px;height:26px;border-radius:50%;background:var(--red)}
.brand-name{font-family:"Barlow Semi Condensed",sans-serif;font-weight:700;font-size:26px;color:var(--teal)}
.menu{display:flex;gap:30px;font-size:14px;font-weight:500;align-items:center}
.menu .active{color:var(--red)}

.hero{height:520px;position:relative;background:linear-gradient(180deg,#5c8796 0%,#2f6275 55%,#1d4656 100%);color:var(--white);text-align:center}
.hero-inner{position:absolute;top:150px;left:0;right:0}
.hero h1{font-size:50px;text-transform:uppercase;line-height:1.1}
.hero p{margin:14px 0 26px;font-size:17px;opacity:.9}

.intro-box{position:absolute;top:-60px;left:80px;width:1040px;height:130px;display:flex;box-shadow:0 8px 24px rgba(0,0,0,.12)}
.intro-box .tag{width:320px;background:var(--red);color:var(--white);font-size:26px;line-height:1.15;padding:30px 32px;text-transform:uppercase}
.intro-box .copy{flex:1;background:var(--white);padding:34px 40px;color:var(--muted)}

.welcome{height:400px;position:relative;padding:110px 80px 0;display:flex;gap:60px}
.welcome-text{width:480px}
.welcome-text h2{font-size:34px;color:var(--teal);margin:4px 0 14px}
.welcome-text p{color:var(--muted);margin-bottom:12px}
.welcome-photos{flex:1;display:grid;grid-template-columns:1fr 1fr;grid-template-rows:120px 120px;gap:14px}
.welcome-photos .big{grid-row:span 2;background:linear-gradient(160deg,#9cc6d3,#3f7f95)}
.welcome-photos .small1{background:linear-gradient(160deg,#6fa6b8,#24566a)}
.welcome-photos .small2{background:linear-gradient(160deg,#b8d6de,#4d8ca0)}

.video-band{height:280px;background:linear-gradient(180deg,#2c6376,#183c4a);color:var(--white);text-align:center;padding-top:80px}
.video-band h2{font-size:34px;margin-bottom:22px}

.features{height:120px;display:flex;justify-content:center;gap:0;margin:-30px 80px 0;position:relative;background:var(--white);box-shadow:0 6px 20px rgba(0,0,0,.08)}
.feature{flex:1;display:flex;align-items:center;gap:16px;padding:0 34px;border-right:1px solid #e3e6e8}
.feature:last-child{border-right:none}
.feature svg{flex:none}
.feature strong{display:block;color:var(--teal);font-size:15px}
.feature span{color:var(--muted);font-size:13px}

.services{height:350px;background:var(--light);text-align:center;padding-top:70px}
.section-title{font-size:36px;color:var(--teal);margin:4px 0 30px}
.service-cards{display:flex;justify-content:center;gap:26px}
.service-card{width:250px;height:170px;position:relative}
.service-card .label{position:absolute;left:0;right:0;bottom:0;background:rgba(21,53,66,.85);color:var(--white);font-weight:600;padding:8px}

.locations{height:360px;display:flex;align-items:center;gap:60px;padding:0 80px;background:var(--white)}
.locations .photo{width:520px;height:270px;background:linear-gradient(150deg,#8fc0cf,#2f6a7e)}
.locations h2{font-size:36px;color:var(--teal);line-height:1.15;margin:6px 0 14px}
.locations p{color:var(--muted);margin-bottom:20px;max-width:440px}

.pricing{height:490px;background:var(--light);text-align:center;padding-top:60px}
.price-cards{display:flex;justify-content:center;gap:26px}
.price-card{width:300px;background:var(--white);text-align:left;box-shadow:0 4px 14px rgba(0,0,0,.06)}
.price-card .photo{height:170px;position:relative}
.price-card .price{position:absolute;top:14px;right:14px;background:var(--red);color:var(--white);font-weight:700;font-size:15px;padding:4px 12px}
.price-card .body{padding:18px 22px 22px}
.price-card h3{font-size:19px;color:var(--teal);margin-bottom:6px}
.price-card p{color:var(--muted);font-size:13px;margin-bottom:10px}
.price-card .link{color:var(--red);font-weight:700;font-size:13px}

.stats{height:200px;background:var(--red);color:var(--white);position:relative;overflow:hidden;display:flex;align-items:center;padding:0 160px;gap:24px}
.stats .ghost{position:absolute;right:120px;top:30px;font-size:150px;line-height:1;color:rgba(255,255,255,.12)}
.stats .figure{font-size:64px}
.stats p{font-size:17px;max-width:260px;position:relative}

.machine{height:340px;display:flex;gap:40px;padding:50px 80px 0;background:var(--white)}
.machine-text{width:420px}
.machine-text h2{font-size:34px;color:var(--teal);margin:4px 0 14px}
.machine-text ul{list-style:none;column-count:2;font-size:14px;color:var(--muted)}
.machine-text li{padding:4px 0 4px 16px;position:relative}
.machine-text li::before{content:"";position:absolute;left:0;top:13px;width:7px;height:7px;background:var(--red)}
.machine .photo{flex:1;height:240px;background:linear-gradient(180deg,#e9eef0,#c9d6dc);position:relative}
.machine .photo .btn{position:absolute;right:30px;bottom:26px}

.site-footer{height:300px;background:var(--teal);color:#c8d6dc;font-size:14px}
.footer-cols{display:flex;gap:90px;padding:54px 80px 0;height:250px}
.footer-col h4{color:var(--white);font-size:17px;margin-bottom:12px}
.footer-col ul{list-style:none}
.footer-about{width:360px}
.footer-about .brand-name{color:var(--white)}
.footer-about p{margin-top:14px}
.copyright{height:50px;background:var(--teal-dark);display:flex;align-items:center;justify-content:center;font-size:12px}
</style>
</head>
<body>

<div class="top-bar"><span>+501 555 0142</span><span>info@sealarq.com</span></div>

<header class="site-nav">
  <div class="brand"><span class="brand-dot"></span><span class="brand-name">Sea Larq</span></div>
  <nav class="menu">
    <span class="active">Home</span><span>About</span><span>Services</span><span>Pricing</span><span>Destinations</span><span>Contact</span>
    <span class="btn">Book Now</span>
  </nav>
</header>

<section class="hero" role="img" aria-label="Photo of a marlin leaping from the sea beside a charter boat">
  <div class="hero-inner">
    <h1 class="heading">Just giving your appetite for adventure</h1>
    <p>Private fishing and spearfishing charters across the Belize reefs.</p>
    <span class="btn btn-red">Book Now</span>
  </div>
</section>

<section class="welcome">
  <div class="intro-box">
    <div class="tag heading">Spearfishing and Fishing Charters</div>
    <div class="copy">Explore North Belize, Turneffe, Lighthouse Reef and the Blue Hole aboard our fully equipped boats with expert local guides.</div>
  </div>
  <div class="welcome-text">
    <div class="eyebrow">About Our Charters</div>
    <h2 class="heading">Welcome to Sea Larq</h2>
    <p>Sea Larq is a new charter operator offering private trips for anglers and divers who want the best of the Caribbean sea.</p>
    <p>Every trip is planned around you, from the first cast at sunrise to the last dive over the reef wall.</p>
    <span class="btn">Read More</span>
  </div>
  <div class="welcome-photos">
    <div class="photo big" role="img" aria-label="Photo of a guest on a paddle board in clear water"></div>
    <div class="photo small1" role="img" aria-label="Photo of a spearfisher underwater"></div>
    <div class="photo small2" role="img" aria-label="Photo of anglers on a boat deck"></div>
  </div>
</section>

<section class="video-band" role="img" aria-label="Video still of the charter boat out at sea">
  <h2 class="heading">See How We Do It</h2>
  <svg width="70" height="70" viewBox="0 0 70 70" aria-hidden="true"><circle cx="35" cy="35" r="34" fill="#e8262f"/><path d="M28 22 L50 35 L28 48 Z" fill="#fff"/></svg>
</section>

<div class="features">
  <div class="feature">
    <svg width="40" height="40" viewBox="0 0 40 40" aria-hidden="true"><circle cx="20" cy="20" r="19" fill="#e8262f"/><path d="M12 20 l6 6 l11-12" stroke="#fff" stroke-width="3" fill="none"/></svg>
    <div><strong>Best Equipment</strong><span>Modern rods, reels and spearguns on board.</span></div>
  </div>
  <div class="feature">
    <svg width="40" height="40" viewBox="0 0 40 40" aria-hidden="true"><circle cx="20" cy="20" r="19" fill="#e8262f"/><circle cx="20" cy="15" r="5" fill="#fff"/><path d="M10 30 q10-12 20 0 z" fill="#fff"/></svg>
    <div><strong>Expert Guides</strong><span>Local captains who know every reef.</span></div>
  </div>
  <div class="feature">
    <svg width="40" height="40" viewBox="0 0 40 40" aria-hidden="true"><circle cx="20" cy="20" r="19" fill="#e8262f"/><path d="M20 9 a7 7 0 0 1 7 7 c0 6-7 14-7 14 s-7-8-7-14 a7 7 0 0 1 7-7z" fill="#fff"/><circle cx="20" cy="16" r="2.5" fill="#e8262f"/></svg>
    <div><strong>Best Locations</strong><span>Hidden spots far from the crowds.</span></div>
  </div>
</div>

<section class="services">
  <div class="eyebrow">What We Offer</div>
  <h2 class="section-title heading">Our Services</h2>
  <div class="service-cards">
    <div class="service-card photo" style="background:linear-gradient(160deg,#7fb3c4,#24566a)" role="img" aria-label="Photo of an angler holding a catch"><div class="label">Fishing</div></div>
    <div class="service-card photo" style="background:linear-gradient(160deg,#4f97ae,#153542)" role="img" aria-label="Photo of a spearfisher diving"><div class="label">Spearfishing</div></div>
    <div class="service-card photo" style="background:linear-gradient(160deg,#a9d3de,#3f7f95)" role="img" aria-label="Photo of snorkelers over a reef"><div class="label">Snorkeling</div></div>
  </div>
</section>

<section class="locations">
  <div class="photo" role="img" aria-label="Aerial photo of the charter boat over turquoise water"></div>
  <div>
    <div class="eyebrow">Destinations</div>
    <h2 class="heading">Unique &amp; Stunning<br>Locations For You</h2>
    <p>From the atolls of Turneffe to the deep blue of the famous Blue Hole, we take you where the fish are.</p>
    <span class="btn">Explore</span>
  </div>
</section>

<section class="pricing">
  <div class="eyebrow">Choose Your Trip</div>
  <h2 class="section-title heading">Our Pricing</h2>
  <div class="price-cards">
    <div class="price-card">
      <div class="photo" style="background:linear-gradient(160deg,#8fc0cf,#2f6a7e)" role="img" aria-label="Photo of a fishing trip at sea"><span class="price">$450</span></div>
      <div class="body"><h3 class="heading">Fishing Half Day</h3><p>Boat, guide, gear and drinks included for up to six guests.</p><span class="link">Book Now →</span></div>
    </div>
    <div class="price-card">
      <div class="photo" style="background:linear-gradient(160deg,#5fa1b6,#1d4656)" role="img" aria-label="Photo of a spearfishing dive"><span class="price">$600</span></div>
      <div class="body"><h3 class="heading">Spearfishing Full Day</h3><p>Boat, guide, gear and drinks included for up to six guests.</p><span class="link">Book Now →</span></div>
    </div>
    <div class="price-card">
      <div class="photo" style="background:linear-gradient(160deg,#b3dae4,#3f7f95)" role="img" aria-label="Photo of snorkeling at the Blue Hole"><span class="price">$850</span></div>
      <div class="body"><h3 class="heading">Snorkeling Blue Hole</h3><p>Boat, guide, gear and drinks included for up to six guests.</p><span class="link">Book Now →</span></div>
    </div>
  </div>
</section>

<section class="stats">
  <span class="ghost heading">CHARTERS</span>
  <span class="figure heading">95%</span>
  <p>Happy returning guests every season on our charters</p>
</section>

<section class="machine">
  <div class="machine-text">
    <div class="eyebrow">Our Boat</div>
    <h2 class="heading">Our Fishing Machine</h2>
    <ul>
      <li>32 ft center console</li><li>Twin 300 hp engines</li><li>Outriggers and live well</li>
      <li>Dive ladder and tanks</li><li>Shade top and cooler</li><li>GPS and fish finder</li>
    </ul>
  </div>
  <div class="photo" role="img" aria-label="Photo of the white center console fishing boat"><span class="btn btn-red">View Boat</span></div>
</section>

<footer class="site-footer">
  <div class="footer-cols">
    <div class="footer-col footer-about">
      <div class="brand"><span class="brand-dot"></span><span class="brand-name">Sea Larq</span></div>
      <p>Private fishing and spearfishing charters in North Belize.</p>
    </div>
    <div class="footer-col">
      <h4>Quick Links</h4>
      <ul><li>Home</li><li>About</li><li>Services</li><li>Pricing</li><li>Contact</li></ul>
    </div>
    <div class="footer-col">
      <h4>Contact</h4>
      <ul><li>San Pedro, Ambergris Caye</li><li>+501 555 0142</li><li>info@sealarq.com</li><li>www.sealarq.com</li></ul>
    </div>
  </div>
  <div class="copyright">© 2024 Sea Larq. All rights reserved.</div>
</footer>

</body>
</html>
```